Web Design Project

We are looking for a new site design for the OLVEN Summit & Fair. The current site can be found at
http://olvenmeetup-example.org/
The URL is provided for reference. We want a completely different look and layout which is shown in the specifications document.
As part of the design, we want a home page, inside page and a mobile design. The mobile version is to be fairly simple and uncluttered and based on the web design - simple is key and a sample site is referenced in the specifications document.
The design you provide will be implemented in Joomla. The design winner will only need to provide the PSD or Fireworks PNG format. We anticipate creating the template coding in-house.
However, if you have experience creating Joomla templates, please let us know as we may ask you to bid separately to do that phase of the project.
We've provided a specifications document which includes wireframes of the home page, inside page, and mobile version as well as sample sites. We've also included logo files and a picture of the conference city.
For the header at the top, as indicated in the specs document, we want to keep the same overall treatment to every page. We don't want to include images from the city within the header. Instead we want a graphic treatment with the logo. In this manner, the design will be flexiable and can be used for future years.
For the home page, we've indicated that we'd like to have a banner placement implemented within the design. Please place the city image in this area with a nice graphic treatment. This might also be a good place to include the hosting city and date: Veldmoor, VM June 2-5. 2013
The wireframe is provided to illustrate the placement of content and menu items. The exact dimensions of each component can be revised as you see fit. We are also flexiable if you feel we have missed items.

```html
<!DOCTYPE html>
<html lang="en">
<head>
<meta charset="utf-8">
<title>OLVEN Summit &amp; Fair</title>
<link href="https://fonts.googleapis.com/css2?family=Source+Sans+3:ital,wght@0,400;0,600;0,700;1,400&family=Oswald:wght@500&display=swap" rel="stylesheet">
<style>
:root{
  --sky-top:#1d62a8;
  --sky-mid:#5f9fd8;
  --nav-dark:#1f5d9f;
  --nav-mid:#3f83c6;
  --tab:#7cc2f2;
  --ink:#3a3a3a;
  --link:#1f4f85;
  --title:#2a5d94;
  --panel-border:#d6dde6;
  --gold:#d9a21c;
  --gold-dark:#b07b0c;
  --red:#d0201f;
}
*{box-sizing:border-box;margin:0;padding:0}
html,body{width:871px;height:1200px;overflow:hidden}
body{position:relative;font-family:"Source Sans 3",sans-serif;color:var(--ink);
  background:linear-gradient(#fff 0,#fff 900px,#dbe8f5 1000px,#4b86c2 1080px,#1d5a9c 1200px)}
.abs{position:absolute}
.header{left:0;top:0;width:871px;height:300px;
  background:radial-gradient(ellipse 260px 200px at 230px 120px,#fff 0,#d8e9f8 45%,transparent 75%),
  linear-gradient(160deg,var(--sky-top) 0,var(--sky-mid) 55%,#2a6cb0 100%)}
.brand{left:150px;top:80px;width:220px;color:var(--title)}
.brand .mark{display:flex;align-items:center;gap:8px;font-weight:700;font-size:30px;letter-spacing:1px}
.brand .mark i{display:inline-block;width:22px;height:22px;border-radius:50%;background:var(--red)}
.brand p{font-size:13px;margin-top:6px;line-height:1.3}
.photo-lead{left:520px;top:28px;width:258px;height:205px;border-radius:120px 120px 0 0;
  background:linear-gradient(#6d8db1,#2f3f58)}
.photo-guest{left:434px;top:160px;width:76px;height:90px;border-radius:40px 40px 0 0;
  background:linear-gradient(#b9a08a,#4a5a70)}
.wave{left:0;top:200px}
.nav{left:71px;top:282px;width:743px;height:84px;border-radius:0 0 10px 10px;
  background:linear-gradient(var(--nav-mid),var(--nav-dark))}
.nav ul{list-style:none;display:flex;position:absolute;left:34px;bottom:0;height:42px}
.nav li{color:#fff;font-size:14.5px;padding:0 12px;line-height:42px}
.nav li.active{background:var(--tab);border-radius:6px 6px 0 0;color:#1d4f86;padding:0 15px;font-weight:600}
.panel{background:#fff;border:1px solid var(--panel-border);border-radius:6px;box-shadow:0 1px 3px rgba(0,0,0,.15);overflow:hidden}
.panel-head{height:40px;background:linear-gradient(#3e7fc2,#1f5b9c);color:#fff;font-size:16px;line-height:40px;text-align:center}
.mailing .panel-head{text-align:left;padding-left:20px}
.mailing ul{list-style:none;padding:4px 12px}
.mailing li{font-size:11.5px;height:31px;line-height:31px;border-bottom:1px dashed #ddd;padding-left:20px;position:relative}
.mailing li:last-child{border:0}
.mailing li:before{content:"";position:absolute;left:4px;top:11px;border-left:7px solid #4a86c2;border-top:5px solid transparent;border-bottom:5px solid transparent}
.quick p{font-size:11.5px;text-align:center;margin-top:10px;line-height:13px}
.quick a{color:#555;text-decoration:underline}
.weather h3{font-weight:400;font-size:15.5px;color:#666;text-align:center;margin-top:6px}
.weather .temps{left:130px;top:86px;font-size:14px;color:#444;word-spacing:18px}
.weather .day{left:127px;top:110px;font-size:11px;font-weight:600;color:#444}
.social{background:linear-gradient(#3e7fc2,#1f5b9c 40px,#3a2e2a 40px)}
.social .counts{left:55px;top:44px;width:176px;height:103px;border-radius:8px 8px 0 0;
  background:linear-gradient(var(--gold),var(--gold-dark))}
.counts span{position:absolute;left:60px;font-weight:700;font-size:13px;color:#3a2a06}
.social .ico{left:22px;width:13px;height:13px;background:#fff;border-radius:2px}
.banner-city{left:0;top:0;width:498px;height:88px;background:linear-gradient(#c6d6e6,#8aa1b2 55%,#576a58)}
.banner .seal{left:10px;top:100px;width:34px;height:34px;border-radius:50%;background:var(--title)}
.banner .num{left:76px;top:92px;font-family:"Oswald",sans-serif;font-size:40px;color:var(--red);line-height:48px}
.banner .title{left:166px;top:90px;font-weight:700;font-size:29px;color:var(--title);letter-spacing:1.5px;line-height:32px}
.banner .sub{left:167px;top:120px;font-weight:700;font-size:17px;color:var(--title)}
.welcome h2{position:absolute;left:21px;top:20px;width:456px;font-weight:600;font-size:16px;color:var(--title);border-bottom:1px solid #ccc;padding-bottom:6px}
.welcome .lead{position:absolute;left:21px;top:58px;width:458px;font-size:12.3px;line-height:17.8px}
.teaser{position:absolute;top:268px;width:220px}
.teaser a{font-size:13px;color:var(--link);text-decoration:underline}
.teaser p{font-size:11.3px;line-height:17.5px;margin-top:7px}
.btn{display:inline-block;margin-top:11px;background:linear-gradient(#3f7fc1,#1e589a);color:#fff;font-size:14px;padding:4px 12px;border-radius:2px}
.sponsors h2{font-weight:600;font-size:16.5px;color:var(--title);text-align:center;margin-top:11px}
.sponsors hr{border:0;border-top:1px dashed #bbb;margin:10px 10px 0}
.sponsors ul{list-style:none;display:flex;justify-content:space-between;position:absolute;left:50px;right:50px;top:72px}
.sponsors li{font-weight:700;font-size:13px;color:#2a4e7a}
.arrow{top:72px;font-size:28px;color:#aaa;line-height:20px}
.footer{left:0;top:1115px;width:871px;text-align:center;color:#fff;font-size:14px}
.footer .cur{color:#7fc4ff}
.footer p{font-style:italic;margin-top:4px;font-size:13.5px}
</style>
</head>
<body>
<div class="abs header"></div>
<div class="abs brand"><div class="mark"><i></i>OLVEN</div><p>Bedrock &amp; Records<br>OLVEN Summit &amp; Fair<br>Veldmoor VM May 14-17, 2014</p></div>
<div class="abs photo-guest" role="img" aria-label="Photo of a smiling female attendee"></div>
<div class="abs photo-lead" role="img" aria-label="Photo of a man in a business suit"></div>
<svg class="abs wave" width="871" height="200" viewBox="0 0 871 200">
  <path d="M0 45 C200 110 420 40 600 30 S820 50 871 40 L871 200 L0 200Z" fill="#fff"/>
  <path d="M0 45 C200 110 420 40 600 30 S820 50 871 40" fill="none" stroke="#3f7cc0" stroke-width="6"/>
  <path d="M0 60 C220 120 430 60 610 48 S830 70 871 60" fill="none" stroke="#9cc3e8" stroke-width="3"/>
  <path d="M790 80 C850 110 860 160 871 200" fill="none" stroke="#4b86c2" stroke-width="14"/>
</svg>
<nav class="abs nav"><ul><li class="active">Home</li><li>About Us</li><li>Schedule</li><li>Registration</li><li>Exhibitors</li><li>Education</li><li>Sponsors</li><li>Connect</li></ul></nav>

<section class="abs panel mailing" style="left:71px;top:382px;width:231px;height:145px">
  <div class="panel-head">Join Our Mailing List</div>
  <ul><li>desk_info@olvenmail.net</li><li>desk_info@olvenmail.net</li><li>desk_info@olvenmail.net</li></ul>
</section>
<section class="abs panel quick" style="left:73px;top:538px;width:229px;height:92px">
  <div class="panel-head" style="height:32px;line-height:32px">Quick Links</div>
  <p><a>Links goes here</a> / <a>Links goes here</a></p>
  <p><a>Links goes here</a> / <a>Links goes here</a></p>
</section>
<section class="abs panel weather" style="left:73px;top:641px;width:229px;height:148px">
  <div class="panel-head">Current Conditions in</div>
  <h3>Conference City</h3>
  <svg class="abs" style="left:24px;top:68px" width="82" height="68" viewBox="0 0 82 68">
    <g stroke="#f2a71b" stroke-width="2"><line x1="50" y1="2" x2="50" y2="12"/><line x1="72" y1="10" x2="65" y2="17"/><line x1="80" y1="30" x2="70" y2="30"/><line x1="30" y1="10" x2="36" y2="17"/></g>
    <circle cx="50" cy="30" r="14" fill="#f7c232"/>
    <g fill="#d8d8d8"><circle cx="20" cy="45" r="14"/><circle cx="36" cy="38" r="16"/><circle cx="52" cy="48" r="12"/><rect x="8" y="45" width="54" height="15" rx="7"/></g>
  </svg>
  <div class="abs temps">6 24</div>
  <div class="abs day">TOMORROW</div>
</section>
<section class="abs panel social" style="left:73px;top:800px;width:231px;height:146px">
  <div class="panel-head" style="background:none">Stay Connected</div>
  <div class="abs counts"><span style="top:33px">22.265</span><span style="top:68px">15.547</span></div>
  <div class="abs ico" style="top:80px"></div>
  <div class="abs ico" style="top:115px"></div>
</section>

<section class="abs panel banner" style="left:315px;top:382px;width:500px;height:146px">
  <div class="abs banner-city" role="img" aria-label="Panorama of the host city skyline and river bridge"></div>
  <div class="abs seal"></div>
  <div class="abs num">17TH</div>
  <div class="abs title">Summit &amp; Fair</div>
  <div class="abs sub">Veldmoor, VM &nbsp;May 14-17, 2014</div>
</section>

<section class="abs panel welcome" style="left:316px;top:540px;width:497px;height:406px">
  <h2>Welcome to our site</h2>
  <p class="lead">Lorem ipsum dolor sit amet, consectetur adipisicing elit, sed do eiusmod tempor incididunt ut labore et dolore magna aliqua. Ut enim ad minim veniam, quis nostrud exercitation ullamco laboris nisi ut aliquip ex ea commodo consequat. Duis aute irure dolor in reprehenderit in voluptate velit esse cillum dolore eu fugiat nulla pariatur. Excepteur sint occaecat cupidatat non proident, sunt in culpa qui officia deserunt mollit anim id est laborum. Lorem ipsum dolor sit amet, consectetur adipisicing elit, sed do eiusmod tempor incididunt ut labore et dolore magna aliqua. Ut enim ad minim veniam, quis nostrud exercitation ullamco laboris nisi ut aliquip ex ea commodo consequat. Duis aute irure dolor in reprehenderit in voluptate velit esse cillum dolore eu fugiat nulla pariatur. Excepteur sint occaecat cupidatat non proident, sunt in culpa qui officia deserunt mollit anim id est laborum.</p>
  <div class="teaser" style="left:21px"><a>Come to Veldmoor in 2014</a><p>The 2013 Harbourton Summit was a great success - Now is time to start planning for 2014 in Veldmoor.</p><span class="btn">More</span></div>
  <div class="teaser" style="left:262px"><a>Call for Speakers 2014</a><p>The 2014 OLVEN Summit will be held May 14-17 in Veldmoor! &nbsp;Please review the attached document.</p><span class="btn">More</span></div>
</section>

<section class="abs panel sponsors" style="left:74px;top:962px;width:740px;height:130px">
  <h2>Our Renowned Sponsors</h2>
  <hr>
  <span class="abs arrow" style="left:16px">&#8249;</span>
  <ul><li>Norvale</li><li>Brintek</li><li>Qorra</li><li>Delmo</li><li>Trivex</li><li>Kestra</li><li>Haloframe</li><li>Zentrel</li><li>Pyrewave</li></ul>
  <span class="abs arrow" style="right:16px">&#8250;</span>
</section>

<footer class="abs footer">
  <div><span class="cur">Home</span> &nbsp;| About Us | Schedule | Registration | Exhibitors &nbsp;| Education | Sponsors | Connect</div>
  <p>Copyright @ 2013 OLVEN</p>
</footer>
</body>
</html>
```